Bold Loom Custom Apparel Flyer

We're a custom clothing manufacturer marketing to the cycling, triathlon, running and fitness community.
- v
- We offer quick turnaround on custom, small quantity orders
- Our clothing is American Made
- We offer top quality materials and workmanship
- Pricing is extremely competitive
- We market to small businesses, casual athletes, clubs, charitable organizations and race teams
- Athlete owned and operated
-These flyers will be displayed in Bicycle and Running Retail stores, and at events
Photos and information is available at artist's request

Target Market(s)

We offer custom design services for casual clothing(hats, tshirts, jackets) and custom printed apparel for these sports as well.

These flyers will be displayed in Bicycle and Running Retail stores, and at events

Industry/Entity Type

Clothing

Font styles to use
Sans Serif
Other font styles liked:
• Sporty and easy to read

Requirements
Must have
• Please use this link as a guideline to show the design process
• http://order3.velnix-kit.com/Login/en-US/
• pedalboldloom@mailverra.com
• (555)614-2937
• Made in the USA
• NO Minimums
• Youth sizes
• Women's sizes
• Up to 4XL in Race and Club fit
• Custom Cycling, Triathlon, Running, Fitness and Casual Apparel
• Our company color is 801c
Nice to have
• Cant think of right now
Should not have
• Adult content

```html
<!DOCTYPE html>
<html lang="en">
<head>
<meta charset="utf-8">
<title>Bold Loom Custom Apparel – Design Process Flyer</title>
<link rel="stylesheet" href="https://fonts.googleapis.com/css2?family=Roboto+Condensed:wght@400;700;800&family=Roboto:wght@400;500&display=swap">
<style>
  :root{
    --ink:#0c0c0d;
    --panel-black:#111214;
    --paper:#f4f4f4;
    --process-blue:#1ba1d8;
    --process-blue-dark:#0b6f99;
    --accent-orange:#f2a81d;
    --line-grey:#8b8d90;
    --label:#e9e9e9;
    --page-bg:#a9c9e3;
  }
  *{margin:0;padding:0;box-sizing:border-box}
  html,body{width:1200px;height:864px;overflow:hidden;background:var(--page-bg)}
  .flyer{position:relative;width:1200px;height:864px;background:var(--panel-black);overflow:hidden;font-family:"Roboto",Arial,sans-serif}

  /* photo areas */
  .photo{position:absolute}
  .photo--kid{left:0;top:0;width:400px;height:500px;background:linear-gradient(180deg,#3f6b3a 0%,#5c8a45 35%,#6f9a4e 60%,#4e7a38 100%)}
  .photo--trail{left:0;top:514px;width:400px;height:268px;background:linear-gradient(160deg,#2f4a2c 0%,#5a5a3a 45%,#7a5a3c 75%,#5b402b 100%)}
  .photo--field{left:400px;top:0;width:400px;height:180px;background:linear-gradient(180deg,#9fa8c8 0%,#c4a7c0 35%,#6e6aa8 62%,#4b4f8c 100%)}
  .photo--road{left:800px;top:0;width:400px;height:180px;background:linear-gradient(135deg,#6d6e70 0%,#8fa9c4 40%,#b7c8d8 60%,#4d4f52 100%)}
  .band-orange{position:absolute;left:0;top:498px;width:400px;height:16px;background:var(--accent-orange);clip-path:polygon(0 40%,100% 0,100% 70%,0 100%)}

  /* heading band */
  .heading-band{position:absolute;left:400px;top:180px;width:800px;height:80px;background:var(--paper)}
  .heading-band .stripes{position:absolute;left:0;top:0;width:180px;height:80px}
  .heading-title{position:absolute;left:220px;top:8px;font-family:"Roboto Condensed",Arial,sans-serif;font-weight:800;font-size:64px;letter-spacing:4px;color:var(--ink);line-height:1}

  .process-area{position:absolute;left:400px;top:260px;width:800px;height:604px;background:radial-gradient(ellipse at 55% 35%,#26282b 0%,#121314 65%,#0b0b0c 100%)}

  .process-art{position:absolute;left:0;top:0;width:1200px;height:864px}

  .step{position:absolute;transform:translateX(-50%);text-align:center;color:var(--label);font-size:14px;line-height:17px;white-space:nowrap}
  .step b{display:block;font-family:"Roboto Condensed",Arial,sans-serif;font-weight:700;font-size:18px;line-height:19px}

  /* footer */
  .rule-orange{position:absolute;left:0;top:776px;width:905px;height:7px;background:var(--accent-orange);clip-path:polygon(0 40%,100% 0,98% 100%,0 100%)}
  .footer-left{position:absolute;left:0;top:783px;width:400px;height:81px;background:var(--ink)}
  .contact{position:absolute;font-family:"Roboto Condensed",Arial,sans-serif;font-weight:700;color:#fff;display:flex;align-items:center;gap:10px;letter-spacing:1.5px}
  .contact--phone{left:92px;top:804px;font-size:24px}
  .contact--email{left:476px;top:800px;font-size:20px}
  .brand-mark{position:absolute;left:955px;top:745px;width:200px;text-align:center;font-family:"Roboto Condensed",Arial,sans-serif;font-weight:800;font-size:38px;letter-spacing:2px;color:#fff;line-height:1}
</style>
</head>
<body>
<main class="flyer">
  <div class="photo photo--kid" role="img" aria-label="Young rider smiling in a custom team cycling kit on a lakeside lawn"></div>
  <div class="band-orange"></div>
  <div class="photo photo--trail" role="img" aria-label="Cyclocross racer carrying a bike up a wooded dirt trail"></div>
  <div class="photo photo--field" role="img" aria-label="Two cyclists walking bikes through a wildflower field at dusk"></div>
  <div class="photo photo--road" role="img" aria-label="Road racers in matching custom jerseys riding through town"></div>

  <header class="heading-band">
    <svg class="stripes" viewBox="0 0 180 80" aria-hidden="true">
      <polygon points="0,18 10,18 38,80 28,80" fill="var(--ink)"/>
      <polygon points="14,0 30,0 66,80 50,80" fill="var(--ink)"/>
      <polygon points="40,0 56,0 92,80 76,80" fill="var(--ink)"/>
      <polygon points="66,0 82,0 118,80 102,80" fill="var(--ink)"/>
      <polygon points="92,0 108,0 144,80 128,80" fill="var(--process-blue)"/>
      <polygon points="118,0 140,0 176,80 154,80" fill="var(--ink)"/>
    </svg>
    <h1 class="heading-title">DESIGN PROCESS</h1>
  </header>

  <section class="process-area" aria-label="Design process steps"></section>

  <svg class="process-art" viewBox="0 0 1200 864" aria-hidden="true">
    <defs>
      <g id="chev"><circle r="9" fill="#fff"/><path d="M-2,-4 L3,0 L-2,4" fill="none" stroke="#111" stroke-width="1.8"/></g>
    </defs>
    <ellipse cx="808" cy="477" rx="295" ry="168" fill="none" stroke="var(--line-grey)" stroke-width="2"/>
    <path d="M539,390 Q600,478 809,480" fill="none" stroke="var(--line-grey)" stroke-width="2"/>

    <use href="#chev" x="813" y="307"/>
    <g transform="translate(1005 348) rotate(35)"><use href="#chev"/></g>
    <g transform="translate(1094 540) rotate(110)"><use href="#chev"/></g>
    <g transform="translate(922 641) rotate(180)"><use href="#chev"/></g>
    <g transform="translate(692 637) rotate(180)"><use href="#chev"/></g>
    <g transform="translate(523 552) rotate(-120)"><use href="#chev"/></g>
    <use href="#chev" x="666" y="457"/>

    <g stroke="#fff" stroke-width="3" fill="var(--process-blue)">
      <circle cx="683" cy="317" r="38"/><circle cx="906" cy="317" r="38"/>
      <circle cx="1078" cy="392" r="38"/><circle cx="1015" cy="600" r="38"/>
      <circle cx="809" cy="641" r="38"/><circle cx="599" cy="595" r="38"/>
      <circle cx="539" cy="390" r="38"/><circle cx="809" cy="480" r="38"/>
    </g>
    <g fill="none" stroke="var(--process-blue-dark)" stroke-width="1.5">
      <circle cx="683" cy="317" r="41"/><circle cx="906" cy="317" r="41"/>
      <circle cx="1078" cy="392" r="41"/><circle cx="1015" cy="600" r="41"/>
      <circle cx="809" cy="641" r="41"/><circle cx="599" cy="595" r="41"/>
      <circle cx="539" cy="390" r="41"/><circle cx="809" cy="480" r="41"/>
    </g>

    <!-- 1 ideas -->
    <g fill="#fff"><rect x="667" y="300" width="24" height="30" rx="2"/><path d="M688,322 L704,302 L709,306 L693,326 Z" fill="#fff" stroke="var(--process-blue)" stroke-width="1.5"/></g>
    <!-- 2 deposit -->
    <circle cx="906" cy="317" r="20" fill="#fff"/><text x="906" y="327" text-anchor="middle" font-family="Roboto Condensed,sans-serif" font-weight="800" font-size="26" fill="var(--process-blue)">$</text>
    <!-- 3 design -->
    <rect x="1058" y="380" width="40" height="26" rx="2" fill="#fff"/><rect x="1072" y="406" width="12" height="6" fill="#fff"/><rect x="1064" y="412" width="28" height="3" fill="#fff"/><path d="M1070,400 L1092,372" stroke="var(--process-blue)" stroke-width="3"/>
    <!-- 4 order -->
    <g fill="none" stroke="#fff" stroke-width="3"><path d="M993,594 L999,594 L1005,614 L1031,614 L1036,598 L1002,598"/><path d="M1015,578 L1015,592 M1010,587 L1015,592 L1020,587"/></g>
    <circle cx="1009" cy="620" r="3" fill="#fff"/><circle cx="1027" cy="620" r="3" fill="#fff"/>
    <!-- 5 fifty -->
    <text x="809" y="640" text-anchor="middle" font-family="Roboto Condensed,sans-serif" font-weight="800" font-size="20" fill="#fff">50%</text>
    <rect x="791" y="648" width="36" height="10" rx="1" fill="#fff"/>
    <!-- 6 production -->
    <path d="M589,580 L583,586 L587,592 L591,590 L591,606 L607,606 L607,590 L611,592 L615,586 L609,580 L603,583 L595,583 Z" fill="#fff"/>
    <path d="M577,598 Q579,616 595,616 M621,598 Q619,616 603,616" fill="none" stroke="#fff" stroke-width="3"/>
    <!-- 7 delivery -->
    <circle cx="539" cy="374" r="9" fill="#fff"/><rect x="526" y="385" width="26" height="20" fill="#fff"/><path d="M526,392 L552,392" stroke="var(--process-blue)" stroke-width="2"/>
    <!-- 8 reorder -->
    <g fill="none" stroke="#fff" stroke-width="3"><path d="M787,476 L793,476 L799,496 L825,496 L830,480 L796,480"/><path d="M805,470 A10,10 0 1 1 818,472"/></g>
    <circle cx="803" cy="502" r="3" fill="#fff"/><circle cx="821" cy="502" r="3" fill="#fff"/>

    <!-- contact icons -->
    <path d="M75,812 q-4,8 4,18 l4,-2 l-3,-5 l-2,1 q-3,-5 -1,-10 l2,0 l0,-6 z" fill="var(--accent-orange)"/>
  </svg>

  <div class="step" style="left:683px;top:364px"><b>1.</b>Let's talk about<br>your needs and ideas</div>
  <div class="step" style="left:906px;top:362px"><b>2.</b>Custom art deposit<br>of $150 is collected<br>(Will be credited to<br>your clothing order)</div>
  <div class="step" style="left:1080px;top:441px"><b>3.</b>Our team will<br>work with you<br>to create your design</div>
  <div class="step" style="left:1021px;top:648px"><b>4.</b>Place your order</div>
  <div class="step" style="left:813px;top:690px"><b>5.</b>50% deposit is collected.</div>
  <div class="step" style="left:598px;top:640px"><b>6.</b>Production begins</div>
  <div class="step" style="left:541px;top:435px"><b>7.</b>About 4 weeks later,<br>you're enjoying<br>your new clothing</div>
  <div class="step" style="left:813px;top:527px"><b>8.</b>Simple and quick re-order</div>

  <div class="footer-left"></div>
  <div class="rule-orange"></div>
  <div class="contact contact--phone">(555) 208-7416</div>
  <div class="contact contact--email">
    <svg width="20" height="14" viewBox="0 0 20 14" aria-hidden="true"><rect width="20" height="14" fill="var(--accent-orange)"/><path d="M0,0 L10,8 L20,0" fill="none" stroke="var(--ink)" stroke-width="1.6"/></svg>
    pedalboldloom@mailverra.com
  </div>
  <div class="brand-mark">BOLD LOOM</div>
</main>
</body>
</html>
```